I am a newly certified appraiser in three different areas. I am wanting three different cards with a similar design but with different colors for each society.
1. National Guild Stallion Valuers (maroon ink on pale maroon paper)
LOGO provided by Association
2. Global Federation Herdstock Estimator (light green on an off white paper) LOGO provided by Association
3. Northern Council Tillage Machinery (blue ink on a pale blue paper).
web pages of societies:
www.plovaluersnet.example
www.stallionvaluer.example

NOTE: I HAVE INCLUDED MY CERTIFICATION CERTIFICATES FOR YOU TO SEE AND GATHER IDEAS.

I am wanting you to help me with all the design using the different societies logos and incorperate that with my new business.

Additional information to be included please:

PRAIRIEWORTH VALUATIONS LLC

DELIA M. FORSBERG

P.O. BOX 813

EUREKA, MO 63019

573-618-2947

Prairieworth.val@mailbarn.example

THOUGHTS what about on the front of the card stack three pictures of real items.......such as this:

beautiful picture of a Friesian stallion.......(several on the internet)
picture of a Halvor Brinks Tractor...............(several on the internet)
picture of an Angus bull............................(several on the internet)

Then to the right have my information........

Remember put association logos on the back with their definitive names........

THANK YOU ALL SO MUCH LOOKING FORWARD TO SEE WHAT SHOWS UP

Good Morning All,  I wanted to include something I forgot......my designations after my name and the LLC.

So should read:  Delia M. Forsberg  NGTV, NGSV

PRAIRIEWORTH VALUATIONS LLC

Looking forward to seeing all the different ideas.

Thanks,
Delia

I needed to inform all designers about the specific details to put on the card...l

after my name my accreditations:  GFHE  NGTV  NGSV
Also, be sure to put LLC after Prairieworth Valuations LLC
Lastly, don't put the last for digits after the zip code only put 63019

I also would like my name and phone number to stand out.

Thanks so much
Delia

Target Market(s)

Professionals such as bankers and loan officers,attorneys, insurance agencies, all breed associations representing livestock and specifically in the horse associations, equipment companies, and private individuals, etc. Basically anyone that may need to have something to be appraised in my certification areas.
1. Livestock
2. Farm Equiptment
3. Equine (horses)

Industry/Entity Type

Business

Font styles to use
Sans Serif
Decorative

Requirements
Must have
• Would prefer to have brochure cover all areas of my certification and definately include the three different association logos I have provide on my certification papers. In particular the bottom right hand corner of document.

Would like brochure be on front and back of 1 page of paper.
Nice to have
• Logos I provide to be used for the specific area I would be appraising.
Note there may be times where an appraisal may include 2 of my areas or all 3 just depends.

I am letting you design.........
Should not have
• I like a professional look that isn't too busy and give the specifics of "me" a certified appraiser who is educated in my fields of appraising and can provide a detailed professional appraisal not like someone guessing........will be dealing with professional as well as individuals.

```html
<!DOCTYPE html>
<html lang="en">
<head>
<meta charset="utf-8">
<title>Prairieworth Valuations LLC – Business Card</title>
<link rel="stylesheet" href="https://fonts.googleapis.com/css2?family=Arimo:wght@400;700&display=swap">
<style>
  :root {
    --backdrop: #76888a;
    --card-paper: #eff8f7;
    --ink: #1c1c1c;
    --name-blue: #4a9ef0;
    --equine-tone: #c8549e;
    --equine-light: #f4e3ee;
    --machinery-tone: #4f8fe0;
    --machinery-light: #e2eefb;
    --livestock-tone: #e2825c;
    --livestock-light: #f9e9e1;
  }
  * { margin: 0; padding: 0; box-sizing: border-box; }
  html, body {
    width: 1200px;
    height: 800px;
    overflow: hidden;
    background: var(--backdrop);
    font-family: "Arimo", Arial, sans-serif;
    color: var(--ink);
  }
  .stage { position: relative; width: 1200px; height: 800px; }
  .card {
    position: absolute;
    top: 264px;
    width: 477px;
    height: 272px;
    background: var(--card-paper);
  }
  .card--front { left: 114px; }
  .card--back { left: 609px; text-align: center; }

  .certificates {
    position: absolute;
    top: 66px;
    left: 18px;
    display: flex;
    gap: 7px;
  }
  .certificate {
    width: 142px;
    height: 107px;
    border: 7px solid;
  }
  .certificate--equine { border-color: var(--equine-tone); background: linear-gradient(var(--equine-light), #fbf6f8); }
  .certificate--machinery { border-color: var(--machinery-tone); background: linear-gradient(var(--machinery-light), #f6fafe); }
  .certificate--livestock { border-color: var(--livestock-tone); background: linear-gradient(var(--livestock-light), #fdf8f5); }

  .front-name {
    position: absolute;
    top: 204px;
    left: 0;
    width: 100%;
    text-align: center;
    font-weight: 700;
    font-size: 24px;
    letter-spacing: 0.3px;
    color: var(--name-blue);
  }

  .company { margin-top: 52px; font-weight: 700; font-size: 18px; letter-spacing: 0.2px; }
  .holder { margin-top: 16px; font-weight: 700; font-size: 15px; }
  .designations { margin-left: 6px; }
  .address { margin-top: 10px; font-size: 13.5px; line-height: 18px; }
  .contact { margin-top: 8px; font-size: 13.5px; line-height: 18px; }
  .phone { font-weight: 700; }
  .websites { margin-top: 8px; font-size: 13.5px; }
</style>
</head>
<body>
<main class="stage">
  <section class="card card--front">
    <div class="certificates">
      <div class="certificate certificate--equine" role="img" aria-label="Membership certificate of the National Guild Stallion Valuers"></div>
      <div class="certificate certificate--machinery" role="img" aria-label="Membership certificate of the Northern Council Tillage Machinery"></div>
      <div class="certificate certificate--livestock" role="img" aria-label="Membership certificate of the Global Federation Herdstock Estimator"></div>
    </div>
    <p class="front-name">DELIA M. FORSBERG</p>
  </section>

  <section class="card card--back">
    <h1 class="company">PRAIRIEWORTH VALUATIONS LLC</h1>
    <p class="holder">DELIA M. FORSBERG<span class="designations">GFHE NGTV NGSV</span></p>
    <p class="address">P.O. BOX 813<br>EUREKA, MO 63019</p>
    <p class="contact"><span class="phone">573-618-2947</span><br>Prairieworth.val@mailbarn.example</p>
    <p class="websites">www.plovaluersnet.example I www.stallionvaluer.example</p>
  </section>
</main>
</body>
</html>
```